Book Cover for Business Book on Leadership

We are seeking a book cover (front, back, and spine) for a business book that will be 6"x9" vertical. It is a collections of blogs/short essays called Folding Kites: Rehearsing Guidance Each Morning. The author is Dolores Wexham, MA, CSP, ICF.
We would also like a small graphic for the beginning of each chapter.
The title analogy comes from the song "Folding Kites", which goes "Nobody likes me, everybody hates me, I'm going to eat some worms".
The attached files are samples of the look the author likes, but she would like more graphics and smaller words than these.
Target Market(s)
Business professionals or others interested in improving their leadership skills.
Font styles to use
Colors
Designer to choose colors to be used in the design.
Look and feel
Each slider illustrates characteristics of the customer's brand and the style your logo design should communicate.

```html
<!DOCTYPE html>
<html lang="en">
<head>
<meta charset="UTF-8">
<title>Folding Kites: Rehearsing Guidance Each Morning — Book Cover</title>
<link href="https://fonts.googleapis.com/css2?family=Exo+2:wght@500&family=Libre+Baskerville:wght@700&family=Roboto:wght@400&display=swap" rel="stylesheet">
<style>
  :root {
    --paper: #ffffff;
    --title-teal: #149a8f;
    --subtitle-taupe: #8a7b5f;
    --author-ink: #111111;
    --candy-red: #e2343f;
    --candy-orange: #f39a2a;
    --candy-yellow: #f3df3a;
    --candy-green: #5cbf4a;
    --candy-blue: #2aa9c9;
  }
  * { margin: 0; padding: 0; box-sizing: border-box; }
  html, body {
    width: 800px;
    height: 1200px;
    overflow: hidden;
    background: var(--paper);
  }
  .cover {
    position: relative;
    width: 800px;
    height: 1200px;
    background: var(--paper);
  }
  .cover-title {
    position: absolute;
    top: 44px;
    left: 0;
    width: 800px;
    text-align: center;
    font-family: "Exo 2", "Arial Narrow", sans-serif;
    font-weight: 500;
    font-size: 170px;
    line-height: 156px;
    letter-spacing: 2px;
    color: var(--title-teal);
    text-transform: uppercase;
  }
  .cover-title span { display: block; }
  .cover-subtitle {
    position: absolute;
    top: 384px;
    left: 0;
    width: 800px;
    text-align: center;
    font-family: "Libre Baskerville", Georgia, serif;
    font-weight: 700;
    font-size: 45px;
    line-height: 64px;
    color: var(--subtitle-taupe);
  }
  .cover-subtitle span { display: block; }
  .cover-artwork {
    position: absolute;
    top: 626px;
    left: 40px;
    width: 720px;
    height: 356px;
  }
  .cover-author {
    position: absolute;
    top: 1100px;
    left: 0;
    width: 800px;
    text-align: center;
    font-family: "Roboto", Arial, sans-serif;
    font-weight: 400;
    font-size: 32px;
    letter-spacing: 3px;
    color: var(--author-ink);
    text-transform: uppercase;
  }
</style>
</head>
<body>
  <main class="cover">
    <h1 class="cover-title">
      <span>Folding</span>
      <span>Kites</span>
    </h1>
    <p class="cover-subtitle">
      <span>Rehearsing Guidance</span>
      <span>Each Morning</span>
    </p>
    <svg class="cover-artwork" role="img" aria-label="Photograph of a loose pile of multicoloured gummy worm candies on a white background" viewBox="0 0 720 356" xmlns="http://www.w3.org/2000/svg">
      <defs>
        <radialGradient id="candy-glow" cx="50%" cy="50%" r="50%">
          <stop offset="0%" stop-color="#f39a2a" stop-opacity="0.85"/>
          <stop offset="35%" stop-color="#f3df3a" stop-opacity="0.6"/>
          <stop offset="65%" stop-color="#5cbf4a" stop-opacity="0.35"/>
          <stop offset="100%" stop-color="#ffffff" stop-opacity="0"/>
        </radialGradient>
        <linearGradient id="candy-sweep" x1="0" y1="0" x2="1" y2="0">
          <stop offset="0%" stop-color="#e2343f" stop-opacity="0.35"/>
          <stop offset="50%" stop-color="#f39a2a" stop-opacity="0.1"/>
          <stop offset="100%" stop-color="#2aa9c9" stop-opacity="0.35"/>
        </linearGradient>
        <radialGradient id="candy-fade" cx="50%" cy="50%" r="50%">
          <stop offset="70%" stop-color="#ffffff" stop-opacity="1"/>
          <stop offset="100%" stop-color="#ffffff" stop-opacity="0"/>
        </radialGradient>
        <mask id="soft-edge">
          <ellipse cx="360" cy="178" rx="360" ry="178" fill="url(#candy-fade)"/>
        </mask>
      </defs>
      <g mask="url(#soft-edge)">
        <ellipse cx="360" cy="178" rx="360" ry="178" fill="url(#candy-sweep)"/>
        <ellipse cx="360" cy="178" rx="360" ry="178" fill="url(#candy-glow)"/>
      </g>
    </svg>
    <p class="cover-author">Dolores Wexham, MA, CSP, ICF</p>
  </main>
</body>
</html>
```